Wordpress Template/Design for my business

I need a WordPress template to showcase my technical knowledge for my consultancy. Ideally it will use the same formatting your logo that you created for me.

bility to add tabs, and about me section which ill update

good examples:
http://www.plainlymeadowbit.com/
http://lendrickfaulk.com/
http://berttolsmaker.nl/

Target Market(s)

Technical people looking

Industry/Entity Type

Business

Number of Pages Required

3 page

Font styles to use
Other font styles liked:
• See logo

Requirements
Must have
• A

```html
<!DOCTYPE html>
<html lang="en">
<head>
<meta charset="utf-8">
<title>Nimbra – Cloud Consultancy</title>
<link rel="stylesheet" href="https://fonts.googleapis.com/css2?family=Oswald:wght@400;500&family=Roboto:wght@400;500;700&display=swap">
<style>
:root{
  --blue:#3a9ad9;
  --blue-band:#4da6de;
  --blue-dark:#2b86c6;
  --ink:#2c2c2c;
  --ink-soft:#666;
  --grey-bg:#f1f2f3;
  --bar:#1b1b1b;
  --white:#fff;
}
*{margin:0;padding:0;box-sizing:border-box}
html,body{width:672px;height:1200px;overflow:hidden}
body{position:relative;font-family:'Roboto',sans-serif;color:var(--ink);background:var(--white)}
.abs{position:absolute}

/* header */
.site-header{left:0;top:0;width:672px;height:66px;background:var(--white)}
.brand{left:50px;top:20px;display:flex;align-items:center;gap:6px}
.brand-dot{width:16px;height:16px;border-radius:50%;background:var(--blue)}
.brand-name{font-size:18px;font-weight:700;color:var(--blue)}
.main-nav{left:254px;top:29px;display:flex;gap:0;font-size:8.5px;text-transform:uppercase;color:var(--ink)}
.main-nav a{color:inherit;text-decoration:none;margin-right:18px}
.main-nav a.active{color:var(--blue)}
.login-btn{left:566px;top:22px;width:55px;height:20px;border-radius:4px;background:var(--blue);color:var(--white);font-size:9px;display:flex;align-items:center;justify-content:center}

/* hero */
.hero{left:0;top:66px;width:672px;height:294px}
.hero-photo{position:absolute;inset:0;background:linear-gradient(110deg,#1e2329 0%,#3a3f45 45%,#5a5e63 75%,#2f3338 100%)}
.hero-title{right:51px;top:125px;text-align:right;font-family:'Oswald',sans-serif;color:var(--white);text-transform:uppercase;line-height:1}
.hero-title h1{font-size:32px;font-weight:400;letter-spacing:.3px}
.hero-title p{font-size:17px;margin-top:9px}
.hero-arrows{right:51px;top:255px;display:flex;gap:2px}
.hero-arrows span{width:14px;height:17px;background:#1a1a1a;display:flex;align-items:center;justify-content:center}

/* services */
.services{left:0;top:360px;width:672px;height:219px;background:linear-gradient(160deg,#56ade2,#4299d6)}
.section-title-light{left:0;top:36px;width:672px;text-align:center;color:var(--white);font-size:15px;font-weight:500}
.svc-arrow{top:35px}
.service{width:140px;text-align:center;color:var(--white)}
.service-icon{width:60px;height:60px;margin:0 auto;border-radius:50%;background:var(--white);box-shadow:0 2px 6px rgba(0,0,0,.2);display:flex;align-items:center;justify-content:center}
.service h3{font-size:11.5px;font-weight:500;margin-top:13px;text-transform:uppercase}
.service p{font-size:7px;line-height:10px;margin-top:8px;opacity:.9}

/* about */
.about-copy{left:50px;top:619px;width:338px}
.about-copy h2{font-size:15.5px;font-weight:500;color:var(--blue);text-transform:uppercase}
.about-copy h3{font-size:11.5px;font-weight:500;color:var(--ink);text-transform:uppercase;margin-top:3px}
.about-copy p{font-size:7.4px;line-height:13.6px;color:var(--ink-soft);margin-top:6px;text-align:justify}
.read-more{font-size:8px;color:var(--blue);margin-top:10px;display:block}
.about-video{left:399px;top:616px;width:223px;height:142px;border:3px solid var(--white);box-shadow:0 0 3px rgba(0,0,0,.3);background:linear-gradient(135deg,#5d7278,#9fb7bd 55%,#c8d7da)}
.play{position:absolute;left:50%;top:50%;width:38px;height:38px;margin:-19px 0 0 -19px;border-radius:50%;background:rgba(40,40,40,.75);display:flex;align-items:center;justify-content:center}

/* blog */
.blog{left:0;top:785px;width:672px;height:245px;background:var(--grey-bg)}
.section-title-dark{left:0;top:30px;width:672px;text-align:center;font-size:14.5px;font-weight:500;color:#1f2d3d}
.section-title-dark span{color:var(--blue)}
.post{width:177px;top:60px}
.post-img{position:relative;height:109px;border:2px solid var(--white);box-shadow:0 0 2px rgba(0,0,0,.25)}
.date-badge{position:absolute;left:0;top:26px;width:24px;text-align:center;color:var(--white)}
.date-badge .dm{background:var(--blue);height:27px;padding-top:3px;font-size:11px;line-height:11px}
.date-badge .dm small{display:block;font-size:6px;line-height:9px}
.date-badge .yr{background:#2a2a2a;height:27px;font-size:8px;line-height:27px}
.post h4{font-size:9.5px;font-weight:400;margin-top:10px;color:var(--ink)}
.post p{font-size:6.8px;line-height:9.8px;color:var(--ink-soft);margin-top:4px}

/* footer */
.site-footer{left:0;top:1030px;width:672px;height:123px;background:var(--blue)}
.f-col{top:25px;color:var(--white)}
.f-col h5{font-size:9px;font-weight:500;text-transform:uppercase;margin-bottom:12px}
.f-col p,.f-col li{font-size:6.6px;line-height:10px}
.f-links{list-style:none}
.f-links li{line-height:13.6px}
.f-links li::before{content:"▸";font-size:6px;margin-right:4px}
.newsletter-form{display:flex;margin-top:10px}
.newsletter-form .field{width:83px;height:17px;background:var(--white);color:#888;font-size:6px;padding-left:8px;line-height:17px}
.newsletter-form .submit{width:31px;height:17px;background:#1b1b1b;color:var(--white);font-size:7px;line-height:17px;text-align:center}
.social{display:flex;gap:8px;margin-top:9px}
.social span{width:18px;height:18px;border:1px solid rgba(255,255,255,.8);border-radius:50%}
.bottom-bar{left:0;top:1153px;width:672px;height:47px;background:var(--bar);color:var(--white);font-size:7px;text-align:center;line-height:47px}
</style>
</head>
<body>

<header class="site-header abs">
  <div class="brand abs"><span class="brand-dot"></span><span class="brand-name">Nimbra</span></div>
  <nav class="main-nav abs">
    <a class="active" href="#">Home</a><a href="#">About Us</a><a href="#">Services</a><a href="#">Projects</a><a href="#">Blog</a><a href="#">Contact Us</a>
  </nav>
  <div class="login-btn abs">LOGIN</div>
</header>

<section class="hero abs">
  <div class="hero-photo" role="img" aria-label="Businessman holding a tablet with a cloud and network icons floating above it"></div>
  <div class="hero-title abs">
    <h1>Cloud Consultancy</h1>
    <p>IT Specialists in Virtualisation</p>
  </div>
  <div class="hero-arrows abs">
    <span><svg width="6" height="9" viewBox="0 0 6 9"><path d="M5 1L1 4.5 5 8" stroke="#fff" fill="none"/></svg></span>
    <span><svg width="6" height="9" viewBox="0 0 6 9"><path d="M1 1l4 3.5L1 8" stroke="#fff" fill="none"/></svg></span>
  </div>
</section>

<section class="services abs">
  <h2 class="section-title-light abs">OUR SERVICE</h2>
  <svg class="svc-arrow abs" style="left:48px" width="14" height="22" viewBox="0 0 14 22"><path d="M12 1L2 11l10 10" stroke="#fff" stroke-width="1.5" fill="none"/></svg>
  <svg class="svc-arrow abs" style="left:608px" width="14" height="22" viewBox="0 0 14 22"><path d="M2 1l10 10L2 21" stroke="#fff" stroke-width="1.5" fill="none"/></svg>

  <div class="service abs" style="left:43px;top:80px">
    <div class="service-icon"><svg width="22" height="20" viewBox="0 0 22 20"><rect x="1" y="1" width="20" height="13" rx="1" fill="none" stroke="#2b86c6" stroke-width="2"/><rect x="8" y="15" width="6" height="2" fill="#2b86c6"/><rect x="5" y="17" width="12" height="2" fill="#2b86c6"/></svg></div>
    <h3>Design</h3>
    <p>Lorem Ipsum has been the industry's standard dummy text ever since the</p>
  </div>
  <div class="service abs" style="left:192px;top:80px">
    <div class="service-icon"><svg width="24" height="20" viewBox="0 0 24 20"><circle cx="8" cy="11" r="5" fill="none" stroke="#2b86c6" stroke-width="3" stroke-dasharray="2.5 1.5"/><circle cx="8" cy="11" r="1.5" fill="#2b86c6"/><circle cx="18" cy="6" r="3.5" fill="none" stroke="#2b86c6" stroke-width="2.5" stroke-dasharray="2 1.3"/><circle cx="18" cy="15" r="3" fill="none" stroke="#2b86c6" stroke-width="2.2" stroke-dasharray="2 1.3"/></svg></div>
    <h3>Development</h3>
    <p>Lorem Ipsum has been the industry's standard dummy text ever since the</p>
  </div>
  <div class="service abs" style="left:342px;top:80px">
    <div class="service-icon"><svg width="24" height="20" viewBox="0 0 24 20"><path d="M1 1v18h22" stroke="#2b86c6" stroke-width="1.5" fill="none"/><rect x="5" y="10" width="3" height="7" fill="#2b86c6"/><rect x="10" y="5" width="3" height="12" fill="#2b86c6"/><rect x="15" y="8" width="3" height="9" fill="#2b86c6"/><rect x="20" y="12" width="2" height="5" fill="#2b86c6"/></svg></div>
    <h3>Marketing</h3>
    <p>Lorem Ipsum has been the industry's standard dummy text ever since the</p>
  </div>
  <div class="service abs" style="left:491px;top:80px">
    <div class="service-icon"><svg width="26" height="17" viewBox="0 0 26 17"><path d="M6 16a5 5 0 010-10 7 7 0 0113-1 5.5 5.5 0 011 11z" fill="#2b86c6"/></svg></div>
    <h3>Cloud Consultancy</h3>
    <p>Lorem Ipsum has been the industry's standard dummy text ever since the</p>
  </div>
</section>

<section class="about-copy abs">
  <h2>IT Specialists in Virtualisation,</h2>
  <h3>SAN and Cloud Technologies</h3>
  <p>Lorem Ipsum has been the industry's standard dummy text ever since the 1500s, when an unknown printer took a galley of type and scrambled it to make a type specimen book. It has survived not only five centuries, but also the leap into electronic typesetting, remaining essentially unchanged.</p>
  <p>It has survived not only five centuries, but also the leap into electronic typesetting, remaining essentially unchanged. It was popularised in the 1960s with the release of Lettrafold sheets containing Lorem Ipsum passages, and more recently with desktop publishing software like Pagewright Studio including</p>
  <a class="read-more" href="#">Read More »</a>
</section>
<div class="about-video abs" role="img" aria-label="Video still of a businessman in a suit with a cloud and device icons">
  <div class="play"><svg width="14" height="16" viewBox="0 0 14 16"><path d="M2 1l11 7-11 7z" fill="#fff"/></svg></div>
</div>

<section class="blog abs">
  <h2 class="section-title-dark abs">LATEST <span>BLOG</span></h2>

  <article class="post abs" style="left:50px">
    <div class="post-img" role="img" aria-label="Businessman overlaid on a city skyline" style="background:linear-gradient(135deg,#cfd3d6,#8e969c 60%,#5d6469)">
      <div class="date-badge"><div class="dm">02<small>JUN</small></div><div class="yr">2016</div></div>
    </div>
    <h4>Fluxgate 6.2 Edge Services Gateway choices</h4>
    <p>Lorem ipsum dolor sit amet, consectetur adipiscing elit. Sed blandit massa vel mauris sollicitudin dignissim. Lorem ipsum dolor sit amet, consectetur</p>
  </article>

  <article class="post abs" style="left:247px">
    <div class="post-img" role="img" aria-label="Blue globe connected to a network of servers" style="background:linear-gradient(160deg,#0c3f9a,#2a78d8 55%,#9cc8f0)">
      <div class="date-badge"><div class="dm">02<small>JUN</small></div><div class="yr">2016</div></div>
    </div>
    <h4>How to unload policy from a particular</h4>
    <p>Lorem ipsum dolor sit amet, consectetur adipiscing elit. Sed blandit massa vel mauris sollicitudin dignissim. Lorem ipsum dolor sit amet, consectetur</p>
  </article>

  <article class="post abs" style="left:446px">
    <div class="post-img" role="img" aria-label="Man touching a glowing cloud network diagram" style="background:linear-gradient(135deg,#0a1e28,#0f5560 55%,#1a8c96)">
      <div class="date-badge"><div class="dm">02<small>JUN</small></div><div class="yr">2016</div></div>
    </div>
    <h4>Corvane &amp; Helixa Fluxgate proof of concept</h4>
    <p>Lorem ipsum dolor sit amet, consectetur adipiscing elit. Sed blandit massa vel mauris sollicitudin dignissim. Lorem ipsum dolor sit amet, consectetur</p>
  </article>
</section>

<footer class="site-footer abs">
  <div class="f-col abs" style="left:50px">
    <h5>Links</h5>
    <ul class="f-links"><li>Customer Support</li><li>Documentation</li><li>Resources</li><li>General FAQs</li><li>Shortcodes</li></ul>
  </div>
  <div class="f-col abs" style="left:183px;width:128px">
    <h5>Neque Porro Quisquam</h5>
    <p style="text-align:justify">Lorem Ipsum has been the industry's standard dummy text ever since the 1500s, when an unknown printer took</p>
    <p style="text-align:justify;margin-top:4px">a galley of type and scrambled it to make a type specimen book. It has survived not only five centuries, but also the leap into electronic typeset-</p>
  </div>
  <div class="f-col abs" style="left:364px">
    <h5>Get in Touch</h5>
    <p>Address : 418 Harlow Crest Rd,<br>Westfall, NJ</p>
    <p style="margin-top:11px">Phone : 555 018 2740</p>
    <p style="margin-top:11px">Email : hello@nimbra-example.com</p>
  </div>
  <div class="f-col abs" style="left:507px;width:115px">
    <h5>Newsletter</h5>
    <p>Your about us information would fit here nicely.</p>
    <div class="newsletter-form"><span class="field">Email address</span><span class="submit">Submit</span></div>
    <div class="social"><span></span><span></span><span></span></div>
  </div>
</footer>
<div class="bottom-bar abs">Copyright © 2016. All Rights Reserved</div>

</body>
</html>
```